Aviation: Overcast Study Guide Book Cover

We need a book cover (front and back) designed for an Instrument Flight Rules (IFR) study guide used by helicopter and airplane pilots to obtain an instrument rating for a helicopter or airplane. Below is the title and subtitles.

TITLE: OVERCAST STUDY GUIDE
SUBTITLE 1: Checkride Preparation for Airplane and Helicopter Pilots
SUBTITLE 2: Prepare for your Instrument Rating with Confidence

We have also upload recommended text to be included on the back cover. In addition, we included images of similar book covers that we like and ones that we do not like. Below are links to two others books by the author.

https://www.bookvarro.example/Rotorcraft-Exam-Handbook-oral-review/dp/507214638K
https://www.bookvarro.example/Manual-Floatwing-Handling-Lionel-Quarrick/dp/5093742816

Flight students

Aviation

• helicopter and airplane

```html
<!DOCTYPE html>
<html lang="en">
<head>
<meta charset="utf-8">
<title>Overcast Study Guide – Book Cover</title>
<link rel="stylesheet" href="https://fonts.googleapis.com/css2?family=Noto+Serif&family=Tinos&display=swap">
<style>
  :root {
    --backdrop: #9dafc6;
    --navy: #000a28;
    --ink: #1c1c1c;
    --back-ink: #151515;
    --white: #ffffff;
    --sky-top: #7aa0cc;
    --sky-mid: #6f95c2;
    --edge-blue: #6f93bf;
  }
  * { margin: 0; padding: 0; box-sizing: border-box; }
  html, body { width: 1200px; height: 1200px; overflow: hidden; background: var(--backdrop); }
  .cover {
    position: absolute; left: 50px; top: 266px; width: 1100px; height: 668px;
    box-shadow: 0 6px 14px rgba(0,0,0,0.35);
  }
  /* Back cover */
  .back {
    position: absolute; left: 0; top: 0; width: 518px; height: 668px;
    background: radial-gradient(ellipse 62% 58% at 52% 55%, #ffffff 0%, #f4f7fb 35%, #c9d7e8 68%, var(--edge-blue) 100%);
    font-family: "Tinos", "Times New Roman", serif; color: var(--back-ink);
  }
  .back h2 {
    position: absolute; font-weight: normal; font-size: 14.2px; letter-spacing: 0.3px; white-space: nowrap;
  }
  .back p {
    position: absolute; left: 34px; font-size: 11.6px; line-height: 14.3px;
  }
  .back .h-confidence { left: 38px; top: 59px; }
  .back .p-intro { top: 88px; width: 408px; }
  .back .h-content { left: 28px; top: 172px; }
  .back .p-content { top: 206px; width: 408px; }
  .back .h-author { left: 28px; top: 443px; }
  .back .p-author { top: 470px; width: 442px; }
  .topics {
    position: absolute; left: 34px; top: 304px; width: 450px; height: 98px;
    border-collapse: collapse; font-size: 11.6px;
  }
  .topics td { border: 1.6px solid var(--back-ink); padding: 0 4px; vertical-align: middle; }
  .topics tr:nth-child(1) { height: 32px; }
  .topics tr:nth-child(2) { height: 35px; }
  .topics tr:nth-child(3) { height: 31px; }
  /* Spine */
  .spine {
    position: absolute; left: 518px; top: 0; width: 65px; height: 668px; background: var(--navy);
    color: var(--white); font-family: "Noto Serif", "Times New Roman", serif;
  }
  .spine span {
    position: absolute; left: 50%; writing-mode: vertical-rl; transform: translateX(-50%); white-space: nowrap;
  }
  .spine .spine-title { top: 126px; font-size: 23px; letter-spacing: 0.5px; }
  .spine .spine-author { top: 418px; font-size: 15px; }
  /* Front cover */
  .front {
    position: absolute; left: 583px; top: 0; width: 517px; height: 668px;
    font-family: "Noto Serif", "Times New Roman", serif;
  }
  .front-photo {
    position: absolute; inset: 0;
    background: linear-gradient(to bottom, var(--sky-top) 0%, var(--sky-mid) 60%, #4e6f9a 70%, #17284d 80%, var(--navy) 92%);
  }
  .title {
    position: absolute; left: 41px; top: 10px; color: var(--ink); font-weight: normal;
    font-size: 60px; line-height: 58px; letter-spacing: 0.5px;
  }
  .band { position: absolute; left: 0; width: 517px; background: var(--white); }
  .band-thin { top: 136px; height: 8px; }
  .subtitle {
    position: absolute; left: 41px; top: 168px; color: var(--white); font-size: 27px; line-height: 29px;
  }
  .band-tagline { top: 268px; height: 27px; }
  .tagline { position: absolute; left: 41px; top: 272px; font-size: 15.5px; color: var(--ink); letter-spacing: 0.2px; }
  .author-rule { position: absolute; top: 600px; height: 4px; background: var(--white); }
  .author-rule.left { left: 0; width: 159px; }
  .author-rule.right { left: 355px; width: 162px; }
  .author { position: absolute; left: 159px; width: 196px; top: 588px; text-align: center; color: var(--white); font-size: 21px; white-space: nowrap; }
</style>
</head>
<body>
<div class="cover">
  <section class="back">
    <h2 class="h-confidence">PREPARE FOR YOUR IFR CHECK RIDE WITH CONFIDENCE</h2>
    <p class="p-intro">Becoming an instrument rated pilot is one of the most challenging ratings to obtain. This guide helps prepare you to pass your IFR check ride with confidence. The question-and-answer format is easy to follow and provides detailed explanations for expanded knowledge.</p>
    <h2 class="h-content">INCLUDES HELICOPTER AND AIRPLANE SPECIFIC CONTENT</h2>
    <p class="p-content">This guide is designed to prepare an airplane or helicopter pilot the oral portion of the IFR checkride. Unlike other resources, this guide specifically addresses the differences with IFR flight in helicopters. As a dual rated pilot, the author ensures to identify areas of differences between the two categories of IFR flight. The following concepts are addressed within the guide.</p>
    <table class="topics">
      <tr><td>• Preflight Actions</td><td>• Enroute Procedures</td><td>• Aeromedical Factors</td></tr>
      <tr><td>• General IFR Concepts</td><td>• Approach Procedures</td><td>• Weather Fundamentals</td></tr>
      <tr><td>• Departure Procedures</td><td>• IFR Emergences</td><td>• Risk Management</td></tr>
    </table>
    <h2 class="h-author">ABOUT THE AUTHOR:</h2>
    <p class="p-author">About the Author: Lionel Quarrick is ATP rated pilot and helicopter and fixed-wing instructor. Lionel is the owner and operator Vantage Ridge, LLC which does business as Hover Line Aviation and Pike Aviation. Hover Line Aviation provides primary helicopter flight instruction while Pike Aviation provides seaplane flight instruction and tours. In addition to instructing, Lionel has authored other books to include The Rotorcraft Exam Handbook, and Manual of Floatwing Handling. Lionel lives in Kentucky with his beautiful wife Marisol. They have a daughter, Wren, that is dual rated and employed as a captain for a charter company. Prior to learning to fly, Lionel spent several years in the military as a Special Warfare Combat Craft Crewman in the U.S. Navy and Ranger-qualified infantry officer in the U.S. Army.</p>
  </section>

  <section class="spine">
    <span class="spine-title">OVERCAST STUDY GUIDE</span>
    <span class="spine-author">Lionel J. Quarrick</span>
  </section>

  <section class="front">
    <div class="front-photo" role="img" aria-label="Photograph of a white twin-engine turboprop airplane with red and navy stripes in flight against a blue sky, fading to dark navy at the bottom"></div>
    <h1 class="title">OVERCAST<br>STUDY GUIDE</h1>
    <div class="band band-thin"></div>
    <p class="subtitle">Checkride Preparation for<br>Airplane and Helicopter Pilots</p>
    <div class="band band-tagline"></div>
    <p class="tagline">Prepare for your Instrument Rating with Confidence</p>
    <div class="author-rule left"></div>
    <p class="author">Lionel J. Quarrick</p>
    <div class="author-rule right"></div>
  </section>
</div>
</body>
</html>
```